Lumora business card for a plastic surgeon

we need a business card for plastic surgeons that work on a clinic called LUMORA.
we want a clean design and the following informations: name of the doctor, doctor's registration number (called CRM), telephone, address, facebook, instagram.
Colors: white, blue tones, light brown/ coffee

facebook and instagram: lumoracirurgiaestetica

Industry/Entity Type

Business

Contact Information for Business Card

clean design

Font styles to use
Serif
Sans Serif
Other font styles liked:
• helvetica light

Colors
cee9f5
85cae6
85abd2
3276b5
cfeae6
cedeed
eaf1f7

Requirements
Must have
• doctor's name
• identification number (called CRM)
• contact (phone, facebook, instagram, address)

```html
<!DOCTYPE html>
<html lang="pt">
<head>
<meta charset="utf-8">
<title>Lumora – Cartão de Visita</title>
<link href="https://fonts.googleapis.com/css2?family=Cinzel:wght@400&family=Open+Sans:wght@400;600;700&display=swap" rel="stylesheet">
<style>
  :root {
    --stage: #e6e9ec;
    --card-white: #ffffff;
    --blue-deep: #06507a;
    --blue-mid: #0b77a6;
    --blue-bright: #1496c4;
    --blue-light: #85cae6;
    --cyan: #22b3d8;
    --navy: #1d4e79;
    --heading-blue: #1c6ea6;
    --ink: #1f2a33;
  }
  * { margin: 0; padding: 0; box-sizing: border-box; }
  html, body { width: 1200px; height: 864px; overflow: hidden; }
  body {
    background: var(--stage);
    font-family: "Open Sans", Arial, sans-serif;
    position: relative;
  }
  .card {
    position: absolute;
    left: 320px;
    width: 560px;
    height: 320px;
    border-radius: 4px;
    overflow: hidden;
    box-shadow: 0 6px 18px rgba(0,0,0,0.18);
  }
  /* Front side */
  .card-front {
    top: 64px;
    background:
      linear-gradient(90deg,
        var(--blue-deep) 0%, var(--blue-mid) 8%, #086a97 15%, var(--blue-bright) 24%,
        #07628e 33%, var(--blue-mid) 42%, #0a6f9f 50%, var(--blue-bright) 60%,
        #075c88 70%, var(--blue-mid) 80%, #0a6c9c 90%, var(--blue-deep) 100%);
    display: flex;
    flex-direction: column;
    align-items: center;
    justify-content: center;
    color: #fff;
  }
  .front-name {
    font-family: "Cinzel", Georgia, serif;
    font-size: 62px;
    letter-spacing: 2px;
    line-height: 1;
  }
  .front-tagline {
    font-family: "Cinzel", Georgia, serif;
    font-size: 22px;
    letter-spacing: 1px;
    margin-top: 10px;
  }
  /* Back side */
  .card-back {
    top: 424px;
    background: var(--card-white);
  }
  .side-band {
    position: absolute;
    left: 0; top: 0;
    width: 34px; height: 100%;
    background: linear-gradient(180deg, var(--blue-light), var(--cyan) 40%, var(--blue-deep));
  }
  .side-band-cut {
    position: absolute;
    left: 0; top: 0;
    width: 60px; height: 320px;
  }
  .details {
    position: absolute;
    left: 58px; top: 22px;
    color: var(--ink);
    font-size: 14px;
    line-height: 1.45;
  }
  .doctor-name {
    font-size: 19px;
    font-weight: 700;
    color: var(--heading-blue);
    line-height: 1.2;
  }
  .crm { font-size: 13px; margin-bottom: 14px; }
  .address { margin-bottom: 14px; }
  .contact-list { list-style: none; }
  .contact-list li { display: flex; align-items: center; gap: 8px; }
  .contact-list svg { width: 12px; height: 12px; flex: none; }
  .back-brand {
    position: absolute;
    right: 36px; bottom: 30px;
    text-align: center;
  }
  .back-name {
    font-family: "Cinzel", Georgia, serif;
    font-size: 48px;
    color: var(--cyan);
    letter-spacing: 2px;
    line-height: 1;
  }
  .back-tagline {
    font-family: "Cinzel", Georgia, serif;
    font-size: 17px;
    color: var(--navy);
    letter-spacing: 1px;
    margin-top: 8px;
  }
</style>
</head>
<body>
  <section class="card card-front">
    <div class="front-name">LUMORA</div>
    <div class="front-tagline">CIRURGIA PLÁSTICA</div>
  </section>

  <section class="card card-back">
    <div class="side-band"></div>
    <svg class="side-band-cut" viewBox="0 0 60 320" aria-hidden="true">
      <polygon points="34,120 46,110 46,320 34,320" fill="#0b77a6"/>
      <line x1="22" y1="140" x2="46" y2="110" stroke="#ffffff" stroke-width="3"/>
    </svg>

    <div class="details">
      <div class="doctor-name">Doctor Name</div>
      <div class="crm">AB1241ABD</div>
      <div class="address">12345, Address Goes Here<br>Country Name, 123456</div>
      <ul class="contact-list">
        <li>
          <svg viewBox="0 0 12 12"><path d="M2.5 1 L4.5 1 L5.3 3.4 L4 4.4 Q5 6.8 7.6 8 L8.6 6.7 L11 7.5 L11 9.5 Q10.5 11 9 11 Q2 10 1 3 Q1 1.5 2.5 1Z" fill="var(--heading-blue)"/></svg>
          (044)-456-7890
        </li>
        <li>
          <svg viewBox="0 0 12 12"><rect x="0.5" y="2" width="11" height="8" fill="var(--heading-blue)"/><path d="M0.5 2 L6 6.5 L11.5 2" stroke="#fff" stroke-width="1" fill="none"/></svg>
          info@youremail.com
        </li>
        <li>
          <svg viewBox="0 0 12 12"><circle cx="6" cy="6" r="5.5" fill="var(--heading-blue)"/></svg>
          lumoracirurgiaestetica
        </li>
        <li>
          <svg viewBox="0 0 12 12"><circle cx="6" cy="6" r="5.5" fill="var(--heading-blue)"/></svg>
          lumoracirurgiaestetica
        </li>
      </ul>
    </div>

    <div class="back-brand">
      <div class="back-name">LUMORA</div>
      <div class="back-tagline">CIRURGIA PLÁSTICA</div>
    </div>
  </section>
</body>
</html>
```